Halvern Metal Recyclers - www.halvernrecyclers.com.au

I've just rebranded my business and thought what better way to continue with this than getting a website.
It is going to be fairly basic for now. I've attached quite a few images, feel free to use whichever you like.
And pages description is also attached in a .doc file.
Updates

Hi, this is my first time having a website. I am open to anything and trust the experience and ideas you can bring forward. I will look at extending the deadline so I can take my time to give feedback as needed! Thank you all.

Target Market(s)

Mining and industrial and commercial sectors

Coding

Coded - Design and coding required

Number of Pages Required

5+ page

Requirements
Must have
• Logo/Phone number at the top of every page. "Scrap Metal Specialists" tag line at the top of every page.
Nice to have
• Top Navigation.

```html
<!DOCTYPE html>
<html lang="en">
<head>
<meta charset="utf-8">
<title>Halvern Metal Recyclers – Scrap Metal Specialists</title>
<link rel="stylesheet" href="https://fonts.googleapis.com/css2?family=Staatliches&family=Poppins:wght@400;500;600&display=swap">
<style>
:root{
  --navy:#1d3a72;
  --navy-dark:#172f5e;
  --sky:#8fb0e6;
  --grey-head:#8a8a8a;
  --ink:#333;
  --light:#f6f6f6;
  --white:#fff;
}
*{margin:0;padding:0;box-sizing:border-box}
html,body{width:1200px;height:3570px;overflow:hidden}
body{position:relative;background:var(--white);font-family:"Poppins",sans-serif;color:var(--ink)}
.abs{position:absolute}

/* header */
.brand{left:162px;top:22px;color:var(--navy);font-family:"Staatliches",sans-serif;font-size:28px;line-height:30px}
.tagline{left:450px;top:14px;width:300px;text-align:center;color:var(--navy);font-family:"Staatliches",sans-serif;font-size:26px}
.tagline::before,.tagline::after{content:"";display:inline-block;width:16px;height:2px;background:#bbb;vertical-align:middle;margin:0 8px}
.top-phone{right:160px;top:12px;color:var(--navy);font-family:"Staatliches",sans-serif;font-size:27px;display:flex;align-items:center;gap:8px}
.nav{top:72px;left:450px;font-size:13px;color:#444}
.nav a{color:inherit;text-decoration:none;position:absolute;white-space:nowrap;top:8px}
.nav .active{color:var(--navy);font-weight:600}
.nav .cta{background:var(--navy);color:#fff;padding:7px 14px;outline:2px solid var(--navy);outline-offset:2px;top:0;border:1px solid #fff}

/* hero */
.hero{left:0;top:120px;width:1200px;height:577px;background:radial-gradient(ellipse at 80% 35%,#8a7652 0%,#4d4130 35%,#2a241c 70%,#17140f 100%)}
.hero-title{left:162px;top:285px;color:#fff;font-family:"Staatliches",sans-serif;font-size:74px;line-height:74px}
.hero-sub{left:162px;top:365px;color:#fff;font-family:"Staatliches",sans-serif;font-size:50px}
.hero-text{left:162px;top:428px;width:420px;color:#fff;font-size:15px;line-height:24px}
.btn-solid{background:var(--navy);color:#fff;font-size:15px;display:flex;align-items:center;justify-content:center;border:2px solid #fff;outline:2px solid var(--navy)}
.btn-line{border:2px solid var(--navy);color:var(--navy);font-size:15px;display:flex;align-items:center;justify-content:center;background:#fff}
.scroll-down{left:573px;top:670px;width:54px;height:54px;border-radius:50%;background:#fff;box-shadow:0 2px 8px rgba(0,0,0,.2);display:flex;align-items:center;justify-content:center}

/* section heads */
.eyebrow{color:var(--navy);font-size:15px;font-weight:500;letter-spacing:1.5px;display:flex;align-items:center;gap:8px}
.eyebrow::after{content:"";width:32px;height:1px;background:var(--navy)}
.heading{color:var(--grey-head);font-family:"Staatliches",sans-serif;font-size:46px;line-height:52px;font-weight:400}
.copy{font-size:13px;line-height:23px;color:#444}
.copy b{font-weight:600;color:#222}

/* about */
.about-block{left:162px;top:798px;width:284px;height:502px;background:var(--navy)}
.about-photo{left:229px;top:851px;width:404px;height:396px;background:#fff;padding:8px}
.about-photo div{width:100%;height:100%;background:linear-gradient(135deg,#3d4a5e,#d08a3a 45%,#e5b640 70%,#556274)}
.stat{text-align:center;width:120px}
.stat .num{font-size:50px;font-weight:600;color:var(--navy);line-height:56px}
.stat .lbl{font-size:11px;color:#777;line-height:15px}

/* services */
.services-bg{left:0;top:1390px;width:1200px;height:952px;background:var(--light)}
.card{width:277px;height:253px;background:#fff;box-shadow:0 0 4px rgba(0,0,0,.08);padding:5px}
.card .pic{height:196px}
.card p{text-align:center;font-size:13px;font-weight:500;line-height:18px;color:#222;margin-top:9px}

/* benefits */
.benefit-band{left:0;top:2342px;width:1200px;height:578px;background:linear-gradient(90deg,#5e4a38 0%,#a7b9cf 25%,#c5d4e4 50%,#9b9486 70%,#4b4d52 85%,#c29a2c 100%)}
.benefit-card{left:162px;top:2456px;width:466px;height:544px;background:#fff;box-shadow:0 2px 10px rgba(0,0,0,.08)}
.benefit{display:flex;align-items:center;gap:12px;font-size:14px;line-height:18px;color:#222;width:200px}
.benefit .ico{width:54px;height:54px;border-radius:50%;background:var(--navy);flex:none;display:flex;align-items:center;justify-content:center}

/* footer */
.foot-head{color:#fff;font-family:"Staatliches",sans-serif;font-size:20px;padding-bottom:6px;border-bottom:2px solid #4a6197}
.foot-list{list-style:none;color:#fff;font-size:13px;line-height:27px}
.foot-list li::before{content:"»";margin-right:10px}
.contact-item{display:flex;gap:10px;color:#fff;font-size:12.5px;line-height:20px}
.social{display:flex;align-items:center;gap:12px;color:#fff;font-size:13px}
.social span.dot{width:28px;height:28px;border-radius:50%;background:#fff}
.foot-brand{left:807px;top:3270px;width:233px;color:#fff;font-family:"Staatliches",sans-serif;font-size:34px;line-height:36px;text-align:center}
.copyright{left:0;top:3536px;width:1200px;text-align:center;color:#fff;font-size:13px}
</style>
</head>
<body>

<div class="abs brand">Halvern<br>Metal Recyclers</div>
<div class="abs tagline">Scrap Metal Specalists</div>
<div class="abs top-phone">
  <svg width="26" height="26" viewBox="0 0 24 24"><path d="M6.6 10.8c1.4 2.8 3.8 5.1 6.6 6.6l2.2-2.2c.3-.3.7-.4 1-.2 1.1.4 2.3.6 3.6.6.6 0 1 .4 1 1V20c0 .6-.4 1-1 1C10.6 21 3 13.4 3 4c0-.6.4-1 1-1h3.5c.6 0 1 .4 1 1 0 1.3.2 2.5.6 3.6.1.3 0 .7-.2 1z" fill="none" stroke="#999" stroke-width="1.5"/></svg>
  0491 570 156
</div>
<nav class="abs nav">
  <a class="active" style="left:0">Home</a>
  <a style="left:86px">About Us</a>
  <a style="left:190px">Services</a>
  <a style="left:288px">Online Store</a>
  <a style="left:412px">Blog</a>
  <a class="cta" style="left:485px">Contact Us</a>
</nav>

<div class="abs hero" role="img" aria-label="Scrap metal recycling yard with machinery and a large wire cable spool"></div>
<div class="abs hero-title">Scrap Metal</div>
<div class="abs hero-sub">Recycling Industry</div>
<p class="abs hero-text">We provides scrap metal collection and oxy cutting services in the mining, construction, and industrial sectors all around WA.</p>
<div class="abs btn-solid" style="left:163px;top:527px;width:137px;height:39px">Get A Quote</div>
<div class="abs scroll-down"><svg width="22" height="22" viewBox="0 0 22 22"><path d="M11 3v15M4 11l7 7 7-7" fill="none" stroke="#1d3a72" stroke-width="2"/></svg></div>

<div class="abs about-block"></div>
<div class="abs about-photo"><div role="img" aria-label="Two workers in hard hats and hi-vis vests inspecting a yellow machine"></div></div>
<div class="abs eyebrow" style="left:698px;top:821px">ABOUT US</div>
<h2 class="abs heading" style="left:698px;top:846px">Who We Are</h2>
<p class="abs copy" style="left:698px;top:910px;width:340px"><b>Halvern Metal Recyclers</b> sitmli amet, consectetuer adipiscing elit, sed diam nonummy nibhml euismod tincidunt ut laoreet dolore magna aliquam erat mor volutpat. Duis autem vel eum iriure dolor in hendrer in vulputate velit esse molestie.</p>
<p class="abs copy" style="left:698px;top:1035px;width:340px">Ut wisi enim ad minim veniam, quis nostrud exercim tation ullamcorper suscipit lobortis nisl ut aliquip ex ea commodo consequat.</p>
<div class="abs stat" style="left:673px;top:1118px"><div class="num">16</div><div class="lbl">YEARS OF<br>EXPERIENCE</div></div>
<div class="abs stat" style="left:808px;top:1118px"><div class="num">5K</div><div class="lbl">PROJECTS<br>DONE</div></div>
<div class="abs stat" style="left:943px;top:1118px"><div class="num">76</div><div class="lbl">GET<br>AWARDS</div></div>
<div class="abs btn-line" style="left:697px;top:1238px;width:135px;height:43px">Learn More</div>

<div class="abs services-bg"></div>
<div class="abs eyebrow" style="left:162px;top:1484px">SERVICES</div>
<h2 class="abs heading" style="left:162px;top:1506px">Oxy Cutting And<br>Breaking Down Of</h2>
<p class="abs copy" style="left:567px;top:1505px;width:470px;text-align:justify"><b>Halvern Metal Recyclers</b> sitmli amet, consectetuer adipiscing elit, sed diam nonummy nibhml euismod tincidunt ut laoreet dolore magna aliquam erat mor volutpat. Ut wisi enim ad minim veniam, quis nostrud exercim tation suscipit lobor commodo consequat.</p>

<div class="abs card" style="left:162px;top:1640px"><div class="pic" role="img" aria-label="Yellow loader scooping rock at a mine" style="background:linear-gradient(160deg,#9aa8b8,#c9c4b4 40%,#b5714a 65%,#d4b030)"></div><p>LARGE MINING<br>MACHINERY</p></div>
<div class="abs card" style="left:461px;top:1640px"><div class="pic" role="img" aria-label="Excavator grabbing scrap metal with a worker nearby" style="background:linear-gradient(160deg,#b9ccdf,#8f8678 45%,#6e5a4a 75%,#b88a4a)"></div><p>SCRAP METAL CLEAN UP<br>AND REMOVAL</p></div>
<div class="abs card" style="left:761px;top:1640px"><div class="pic" role="img" aria-label="Small excavator clearing trees on a site" style="background:linear-gradient(160deg,#c8d0c4,#6f8258 45%,#4e6a3a 75%,#8aa060)"></div><p>MINESITE CLEAN UPS<br>AND DEMOLITION</p></div>
<div class="abs card" style="left:162px;top:1917px"><div class="pic" role="img" aria-label="Worker cutting steel structures outdoors" style="background:linear-gradient(160deg,#b9c2b8,#5d6050 45%,#3e3a34 75%,#7a5c40)"></div><p>SUBSEA - JETTY'S, BARGES, PYLONS,<br>BOATS, ANCHORS, CHAIN</p></div>
<div class="abs card" style="left:461px;top:1917px"><div class="pic" role="img" aria-label="Large conveyor infrastructure at a minesite" style="background:linear-gradient(160deg,#7fa8d8,#b9c8d4 40%,#8a7c66 70%,#5e6a4a)"></div><p>LARGE MINESITE<br>INFRASTRUCTURE</p></div>
<div class="abs card" style="left:761px;top:1917px"><div class="pic" role="img" aria-label="Workers on an elevated work platform beside a building" style="background:linear-gradient(160deg,#d8dde2,#9aa2ac 40%,#2a4ea8 65%,#c9cdd2)"></div><p>EWP AND HIGH<br>RISK WORK</p></div>
<div class="abs btn-line" style="left:514px;top:2209px;width:172px;height:43px">View All Services</div>

<div class="abs benefit-band" role="img" aria-label="Operator seated in the cab of a yellow excavator under a blue sky"></div>
<div class="abs benefit-card"></div>
<div class="abs eyebrow" style="left:206px;top:2504px">BENEFITS</div>
<h2 class="abs heading" style="left:206px;top:2527px">Why Choose Us</h2>
<p class="abs copy" style="left:206px;top:2595px;width:370px"><b>Halvern Metal Recyclers</b> sitmli amet, consectetuer duis autem vel eum velit esse molestie.</p>
<div class="abs benefit" style="left:205px;top:2662px"><span class="ico"><svg width="26" height="26" viewBox="0 0 26 26"><circle cx="13" cy="9" r="4" fill="none" stroke="#fff" stroke-width="1.5"/><path d="M5 22c1-5 4-7 8-7s7 2 8 7" fill="none" stroke="#fff" stroke-width="1.5"/></svg></span>Expertise in<br>Mining Industry</div>
<div class="abs benefit" style="left:408px;top:2662px"><span class="ico"><svg width="26" height="26" viewBox="0 0 26 26"><circle cx="13" cy="13" r="9" fill="none" stroke="#fff" stroke-width="1.5"/><path d="M13 8v5l4 3" fill="none" stroke="#fff" stroke-width="1.5"/></svg></span>Quicker<br>Response Time</div>
<div class="abs benefit" style="left:205px;top:2745px"><span class="ico"><svg width="26" height="26" viewBox="0 0 26 26"><path d="M4 14l5-4 4 3 4-3 5 4-5 4-4-2-4 2z" fill="none" stroke="#fff" stroke-width="1.5"/></svg></span>Most Trusted<br>In WP</div>
<div class="abs benefit" style="left:408px;top:2745px"><span class="ico"><svg width="26" height="26" viewBox="0 0 26 26"><circle cx="13" cy="13" r="8" fill="none" stroke="#fff" stroke-width="1.5"/><path d="M13 8v10M10 11h5a2 2 0 010 4h-4" fill="none" stroke="#fff" stroke-width="1.5"/></svg></span>Cost<br>Effectiveness</div>
<div class="abs benefit" style="left:205px;top:2827px"><span class="ico"></span>Deadline Driven<br>Schedule</div>
<div class="abs benefit" style="left:408px;top:2827px"><span class="ico"></span>Dedicated<br>Towards Work</div>
<div class="abs btn-line" style="left:205px;top:2912px;width:139px;height:43px">Get A Quote</div>

<svg class="abs" style="left:0;top:3080px" width="1200" height="490" viewBox="0 0 1200 490">
  <polygon points="90,90 261,15 845,60" fill="var(--sky)"/>
  <polygon points="0,110 261,25 1200,140 1200,490 0,490" fill="var(--navy)"/>
</svg>
<div class="abs foot-head" style="left:162px;top:3260px;width:125px">Quick Links</div>
<ul class="abs foot-list" style="left:162px;top:3305px">
  <li>Home</li><li>About Us</li><li>Services</li><li>Online Store</li><li>Blog</li><li>Contact &nbsp;Us</li>
</ul>
<div class="abs foot-head" style="left:356px;top:3260px;width:176px">Contact Details</div>
<div class="abs contact-item" style="left:356px;top:3312px"><svg width="14" height="18" viewBox="0 0 14 18"><path d="M7 1a6 6 0 016 6c0 4-6 10-6 10S1 11 1 7a6 6 0 016-6z" fill="#fff"/><circle cx="7" cy="7" r="2" fill="var(--navy)"/></svg><span>74 Forge Lane,<br>Kwinana WA 6167</span></div>
<div class="abs contact-item" style="left:356px;top:3365px"><svg width="14" height="14" viewBox="0 0 24 24"><path d="M6.6 10.8c1.4 2.8 3.8 5.1 6.6 6.6l2.2-2.2c.3-.3.7-.4 1-.2 1.1.4 2.3.6 3.6.6.6 0 1 .4 1 1V20c0 .6-.4 1-1 1C10.6 21 3 13.4 3 4c0-.6.4-1 1-1h3.5c.6 0 1 .4 1 1 0 1.3.2 2.5.6 3.6.1.3 0 .7-.2 1z" fill="#fff"/></svg><span><b style="font-weight:600">Phone</b><br>0491570156</span></div>
<div class="abs contact-item" style="left:356px;top:3423px"><svg width="14" height="12" viewBox="0 0 14 12"><rect x="0" y="1" width="14" height="10" fill="#fff"/><path d="M0 1l7 6 7-6" fill="none" stroke="var(--navy)" stroke-width="1.2"/></svg><span><b style="font-weight:600">Email</b><br>inquiry@halvernrecyclers.com.au</span></div>
<div class="abs foot-head" style="left:631px;top:3260px;width:104px">Follow Us</div>
<div class="abs social" style="left:631px;top:3316px"><span class="dot"></span>Newsfeed</div>
<div class="abs social" style="left:631px;top:3360px"><span class="dot"></span>Updates</div>
<div class="abs social" style="left:631px;top:3404px"><span class="dot"></span>Videos</div>
<div class="abs foot-brand">Halvern<br>Metal Recyclers</div>
<div class="abs copyright">© 2022 HALVERN METAL RECYCLERS. All Rights Reserved.</div>

</body>
</html>
```